Real Estate Business Cards

Looking for a clean, sharp and professional look for our Real Estate investment Fund that invests in Multi Family Apartment buildings.

Target Market(s)

Real Estate Fund

Industry/Entity Type

Real Estate

Contact Information for Business Card

Company Description: Real Estate Investment Fund
Company Name: RKW Holdings
Name: Marcus Olvane
Cell: (917) 482-0657
Email: marcus@rkwholdings-example.com
Website: www.rkwholdings-example.com
Address: 418, 9th Street, Brooklyn NY 11218

Colors

Designer to choose colors to be used in the design.

Requirements
Nice to have
• Colors to match logo

```html
<!DOCTYPE html>
<html lang="en">
<head>
<meta charset="utf-8">
<title>RKW Holdings – Business Cards</title>
<link href="https://fonts.googleapis.com/css2?family=Lato:wght@400;700&display=swap" rel="stylesheet">
<style>
  :root {
    --stage: #ece9e4;
    --card-gray: #5a5a5c;
    --paper: #ffffff;
    --ink-light: #ffffff;
    --ink-dark: #444446;
    --accent: #1f6fb2;
  }
  * { margin: 0; padding: 0; box-sizing: border-box; }
  html, body { width: 1200px; height: 902px; overflow: hidden; }
  body {
    background: var(--stage);
    font-family: "Lato", Arial, sans-serif;
    position: relative;
  }
  .card {
    position: absolute;
    top: 131px;
    width: 380px;
    height: 640px;
    border-radius: 26px;
    overflow: hidden;
    background: var(--card-gray);
    box-shadow: 0 10px 24px rgba(0,0,0,0.18);
  }
  .card--front { left: 190px; }
  .card--back { left: 630px; }
  .card__split { position: absolute; inset: 0; width: 100%; height: 100%; }

  .brand {
    position: absolute;
    display: flex;
    flex-direction: column;
    align-items: center;
  }
  .brand__name {
    font-weight: 400;
    text-transform: uppercase;
    white-space: nowrap;
  }
  .card--front .brand { left: 214px; top: 66px; width: 156px; gap: 10px; }
  .card--front .brand__mark { width: 30px; height: 30px; background: var(--accent); }
  .card--front .brand__name { color: var(--ink-dark); font-size: 18px; letter-spacing: 1px; }
  .card--back .brand { left: 0; right: 0; top: 250px; gap: 14px; }
  .card--back .brand__mark { width: 34px; height: 34px; background: var(--ink-light); }
  .card--back .brand__name { color: var(--ink-light); font-size: 30px; letter-spacing: 1.5px; }

  .holder {
    position: absolute;
    left: 28px;
    top: 318px;
    color: var(--ink-light);
    font-weight: 700;
    font-size: 20px;
    letter-spacing: 1px;
  }
  .contacts {
    position: absolute;
    left: 28px;
    top: 372px;
    list-style: none;
    color: var(--ink-light);
    font-size: 14px;
    letter-spacing: 0.3px;
    line-height: 24px;
  }
  .contacts li { display: flex; align-items: center; gap: 8px; white-space: nowrap; }
  .contacts svg { width: 14px; height: 14px; flex: none; }
  .address {
    position: absolute;
    left: 28px;
    top: 470px;
    color: var(--ink-light);
    font-size: 14px;
    letter-spacing: 0.5px;
    line-height: 24px;
    font-style: normal;
  }
  .tagline {
    position: absolute;
    left: 30px;
    bottom: 36px;
    color: var(--ink-light);
    font-size: 17px;
    font-style: italic;
    letter-spacing: 0.5px;
  }
</style>
</head>
<body>
  <section class="card card--front" aria-label="Business card front">
    <svg class="card__split" viewBox="0 0 380 640" aria-hidden="true">
      <polygon points="150,0 380,0 380,610" fill="var(--paper)"/>
    </svg>
    <div class="brand">
      <span class="brand__mark"></span>
      <span class="brand__name">RKW Holdings</span>
    </div>
    <h1 class="holder">Marcus Olvane</h1>
    <ul class="contacts">
      <li>
        <svg viewBox="0 0 14 14" aria-hidden="true"><circle cx="7" cy="7" r="6.5" fill="none" stroke="#fff"/><path d="M4.5 3.8h1.6l.7 1.8-.9.7a5 5 0 0 0 2 2l.7-.9 1.8.7v1.6a.8.8 0 0 1-.8.7A6 6 0 0 1 3.8 4.6a.8.8 0 0 1 .7-.8z" fill="#fff"/></svg>
        (917) 482-0657
      </li>
      <li>
        <svg viewBox="0 0 14 14" aria-hidden="true"><circle cx="7" cy="7" r="6.5" fill="none" stroke="#fff"/><rect x="3.5" y="4.8" width="7" height="4.6" fill="none" stroke="#fff" stroke-width="0.9"/><path d="M3.5 4.8 7 7.6l3.5-2.8" fill="none" stroke="#fff" stroke-width="0.9"/></svg>
        marcus@rkwholdings-example.com
      </li>
      <li>
        <svg viewBox="0 0 14 14" aria-hidden="true"><circle cx="7" cy="7" r="6.5" fill="none" stroke="#fff"/><circle cx="7" cy="7" r="3.6" fill="none" stroke="#fff" stroke-width="0.8"/><path d="M3.4 7h7.2M7 3.4v7.2" stroke="#fff" stroke-width="0.8"/></svg>
        www.rkwholdings-example.com
      </li>
    </ul>
    <address class="address">418, 9th Street<br>Brooklyn NY 11218</address>
  </section>

  <section class="card card--back" aria-label="Business card back">
    <div class="brand">
      <span class="brand__mark"></span>
      <span class="brand__name">RKW Holdings</span>
    </div>
    <p class="tagline">Real Estate Investment Fund</p>
  </section>
</body>
</html>
```